Construction Company

Design a clutter free business card, it can be double-sided utilizing the logo for BNX Ltd simple with all relevant contact information.

Please also a letterhead design to function for the purposes of invoicing, all mail requirements, with header to be distinctive while the footer ties page together and incorporates all necessary information.

For now, please use generic / dummy text and when a winner is selected, I will disclose the contact information.

Hi Designers! Please read the updated brief which includes the design of a business card and letterhead. Thank you!

```html
<!DOCTYPE html>
<html lang="en">
<head>
<meta charset="utf-8">
<title>BNX Ltd Stationery</title>
<link rel="stylesheet" href="https://fonts.googleapis.com/css2?family=Lato:wght@400;700;900&family=Roboto+Condensed:wght@300;400&display=swap">
<style>
:root{
  --navy:#213a86;
  --gold:#b99633;
  --ink:#4d4d4d;
  --muted:#6b6b6b;
  --paper:#ffffff;
  --backdrop:#d8e3ef;
}
*{margin:0;padding:0;box-sizing:border-box}
html,body{width:1200px;height:831px;overflow:hidden;background:var(--backdrop)}
.canvas{position:relative;width:1200px;height:831px}
.sheet{position:absolute;background:var(--paper);box-shadow:0 3px 10px rgba(40,60,100,.28);overflow:hidden}
.wordmark{position:absolute;font-family:'Lato',sans-serif;font-weight:900;color:var(--navy);white-space:nowrap;letter-spacing:.5px;line-height:1}
.wordmark.on-navy{color:#fff}
.footer-band{position:absolute;left:0;bottom:0;width:100%}
.icon{display:inline-block;vertical-align:middle}

/* Letterhead */
.letterhead{left:117px;top:111px;width:430px;height:609px}
.letterhead .wordmark{left:39px;top:44px;font-size:34px}
.lh-contact{position:absolute;right:42px;top:33px;text-align:right;font-family:'Lato',sans-serif;font-weight:400;font-size:8.2px;color:var(--muted);line-height:9.6px;font-style:normal}
.lh-contact .addr{margin-bottom:4px}
.lh-contact .row{height:10.8px;line-height:10.8px}
.lh-contact .row .icon{margin-left:5px}
.accent{color:var(--gold)}
.letter-body{position:absolute;left:39px;top:200px;width:349px;font-family:'Roboto Condensed',sans-serif;font-weight:300;font-size:9.7px;line-height:15px;color:var(--ink);text-align:justify}
.letter-body p{margin-bottom:14.8px}
.letter-body .salutation{margin-bottom:13px}
.closing{position:absolute;left:39px;top:495px;font-family:'Roboto Condensed',sans-serif;font-weight:300;font-size:10px;color:var(--ink)}
.signature{position:absolute;left:37px;top:514px;width:36px;height:23px;border-radius:3px;background:linear-gradient(90deg,rgba(185,150,51,.18),rgba(185,150,51,.32))}

/* Business card front */
.card-front{left:635px;top:112px;width:183px;height:105px}
.card-front .wordmark{right:11px;top:14px;font-size:17px}
.card-name{position:absolute;left:11px;top:51px;font-family:'Lato',sans-serif;font-weight:900;font-size:8.4px;color:var(--navy)}
.card-title{position:absolute;left:11px;top:61px;font-family:'Lato',sans-serif;font-size:4.4px;color:var(--gold)}
.card-rule{position:absolute;left:11px;right:11px;top:70px;border-top:.6px solid #666}
.card-contacts{position:absolute;left:11px;top:74px;font-family:'Lato',sans-serif;font-size:4.4px;color:#555;line-height:6.6px}
.card-contacts .icon{margin-right:3px}
.card-address{position:absolute;right:11px;top:80.5px;text-align:right;font-family:'Lato',sans-serif;font-size:4.4px;color:#555;line-height:6.6px}

/* Business card back */
.card-back{left:904px;top:111px;width:182px;height:104px;background:var(--navy)}
.card-back .wordmark{left:0;width:100%;text-align:center;top:38px;font-size:27px}

/* Envelope back */
.envelope-back{left:635px;top:248px;width:451px;height:226px}
.flap{position:absolute;left:0;top:0}
.envelope-back .wordmark{left:0;width:100%;text-align:center;top:26px;font-size:16px}

/* Envelope front */
.envelope-front{left:635px;top:494px;width:451px;height:226px}
.envelope-front .wordmark{left:42px;top:48px;font-size:34px}
.env-contact{position:absolute;left:42px;top:146px;font-family:'Lato',sans-serif;font-size:7.6px;color:var(--muted);line-height:8.8px;font-style:normal}
.env-contact .addr{margin-bottom:3px}
.env-contact .row{height:9.7px;line-height:9.7px}
.env-contact .row .icon{margin-right:5px}
</style>
</head>
<body>
<main class="canvas">

  <section class="sheet letterhead" aria-label="Letterhead">
    <div class="wordmark">BNX Ltd</div>
    <address class="lh-contact">
      <div class="addr">1234 First Line Address<br>5678 Second Line Address</div>
      <div class="row">(777) 888-7777<svg class="icon" width="7" height="7" viewBox="0 0 10 10"><path d="M2 1l2 2-1 1.3c.6 1.2 1.5 2.1 2.7 2.7L7 6l2 2-1.2 1.3C4.5 9 1 5.5.7 2.2z" fill="var(--gold)"/></svg></div>
      <div class="row">info@yourmail.com<svg class="icon" width="7" height="7" viewBox="0 0 10 10"><rect x=".5" y="2" width="9" height="6" fill="var(--gold)"/><path d="M.5 2l4.5 3.5L9.5 2" stroke="#fff" stroke-width=".8" fill="none"/></svg></div>
      <div class="row">www.<span class="accent">yourwebsite</span>.com<svg class="icon" width="7" height="7" viewBox="0 0 10 10"><circle cx="5" cy="5" r="4.2" fill="none" stroke="var(--gold)" stroke-width=".9"/><path d="M.8 5h8.4M5 .8c-2.4 2.6-2.4 5.8 0 8.4M5 .8c2.4 2.6 2.4 5.8 0 8.4" stroke="var(--gold)" stroke-width=".7" fill="none"/></svg></div>
    </address>

    <div class="letter-body">
      <p class="salutation">Dear Sir/Mam,</p>
      <p>Contrary to popular belief, Lorem Ipsum is not simply random text. It has roots in a piece of classical Latin literature from 45 BC, making it over 2000 years old. Martin Delacroix, a Latin professor at Westbrook Hill College in Ashford, looked up one of the more obscure Latin words, consectetur.</p>
      <p>Lorem Ipsum comes from sections 1.10.32 and 1.10.33 of "de Rebus Bonis et Malis" (The Extremes of Good and Evil) by Varellus, written in 45 BC. This book is a treatise on the theory of ethics, very popular during the Renaissance. The first line of Lorem Ipsum.</p>
      <p>The standard chunk of Lorem Ipsum used since the 1500s is reproduced below for those interested. Sections 1.10.32 and 1.10.33 from "de Rebus Bonis et Malis" by Varellus are also reproduced in their exact original.</p>
      <p>The standard chunk of Lorem Ipsum used since the 1500s is reproduced below for those interested.</p>
    </div>
    <div class="closing">Best Regards</div>
    <div class="signature" role="img" aria-label="Handwritten signature of Reyes"></div>

    <svg class="footer-band" width="430" height="16" viewBox="0 0 430 16" preserveAspectRatio="none">
      <polygon points="0,3 108,3 106,6.5 0,6.5" fill="var(--gold)"/>
      <polygon points="110,3 219,3 217,6.5 108,6.5" fill="var(--navy)"/>
      <polygon points="222,3 331,3 329,6.5 220,6.5" fill="var(--gold)"/>
      <rect x="0" y="10.5" width="430" height="5.5" fill="var(--navy)"/>
      <polygon points="334,16 345,0 430,0 430,16" fill="var(--navy)"/>
    </svg>
  </section>

  <section class="sheet card-front" aria-label="Business card front">
    <div class="wordmark">BNX Ltd</div>
    <div class="card-name">DANIEL REYES</div>
    <div class="card-title">Founder &amp; CEO</div>
    <div class="card-rule"></div>
    <div class="card-contacts">
      <div><svg class="icon" width="4" height="4" viewBox="0 0 10 10"><path d="M2 1l2 2-1 1.3c.6 1.2 1.5 2.1 2.7 2.7L7 6l2 2-1.2 1.3C4.5 9 1 5.5.7 2.2z" fill="var(--gold)"/></svg>(777) 888-7777</div>
      <div><svg class="icon" width="4" height="4" viewBox="0 0 10 10"><rect x=".5" y="2" width="9" height="6" fill="var(--gold)"/></svg>info@yourmail.com</div>
      <div><svg class="icon" width="4" height="4" viewBox="0 0 10 10"><circle cx="5" cy="5" r="4" fill="none" stroke="var(--gold)" stroke-width="1.2"/></svg>www.<span class="accent">yourwebsite</span>.com</div>
    </div>
    <div class="card-address">1234 First Line Address<br>5678 Second Line Address</div>
    <svg class="footer-band" width="183" height="6" viewBox="0 0 183 6" preserveAspectRatio="none">
      <polygon points="0,0 45,0 44,1.6 0,1.6" fill="var(--gold)"/>
      <polygon points="46,0 92,0 91,1.6 45,1.6" fill="var(--navy)"/>
      <polygon points="93,0 140,0 139,1.6 92,1.6" fill="var(--gold)"/>
      <rect x="0" y="3.2" width="183" height="2.8" fill="var(--navy)"/>
      <polygon points="141,6 145,0 183,0 183,6" fill="var(--navy)"/>
    </svg>
  </section>

  <section class="sheet card-back" aria-label="Business card back">
    <div class="wordmark on-navy">BNX Ltd</div>
  </section>

  <section class="sheet envelope-back" aria-label="Envelope back">
    <svg class="flap" width="451" height="66" viewBox="0 0 451 66">
      <path d="M0 0H451L447 40Q445 66 420 66H31Q6 66 4 40Z" fill="var(--navy)"/>
    </svg>
    <div class="wordmark on-navy">BNX Ltd</div>
  </section>

  <section class="sheet envelope-front" aria-label="Envelope front">
    <div class="wordmark">BNX Ltd</div>
    <address class="env-contact">
      <div class="addr">1234 First Line Address<br>5678 Second Line Address</div>
      <div class="row"><svg class="icon" width="7" height="7" viewBox="0 0 10 10"><path d="M2 1l2 2-1 1.3c.6 1.2 1.5 2.1 2.7 2.7L7 6l2 2-1.2 1.3C4.5 9 1 5.5.7 2.2z" fill="var(--gold)"/></svg>(777) 888-7777</div>
      <div class="row"><svg class="icon" width="7" height="7" viewBox="0 0 10 10"><rect x=".5" y="2" width="9" height="6" fill="var(--gold)"/><path d="M.5 2l4.5 3.5L9.5 2" stroke="#fff" stroke-width=".8" fill="none"/></svg>info@yourmail.com</div>
      <div class="row"><svg class="icon" width="7" height="7" viewBox="0 0 10 10"><circle cx="5" cy="5" r="4.2" fill="none" stroke="var(--gold)" stroke-width=".9"/><path d="M.8 5h8.4M5 .8c-2.4 2.6-2.4 5.8 0 8.4M5 .8c2.4 2.6 2.4 5.8 0 8.4" stroke="var(--gold)" stroke-width=".7" fill="none"/></svg>www.<span class="accent">yourwebsite</span>.com</div>
    </address>
    <svg class="footer-band" width="451" height="16" viewBox="0 0 451 16" preserveAspectRatio="none">
      <polygon points="0,3 113,3 111,6.5 0,6.5" fill="var(--gold)"/>
      <polygon points="115,3 231,3 229,6.5 113,6.5" fill="var(--navy)"/>
      <polygon points="234,3 347,3 345,6.5 232,6.5" fill="var(--gold)"/>
      <rect x="0" y="10.5" width="451" height="5.5" fill="var(--navy)"/>
      <polygon points="350,16 361,0 451,0 451,16" fill="var(--navy)"/>
    </svg>
  </section>

</main>
</body>
</html>
```